Fancy flyer to entice High School Students

http://quillmarsh.com needs a marketing slick/flyer to pass out. The marketing text is below(feel free to place where you think appropriate).

* 8th grade to 12th grade (or 8th graders to 12th graders)
* Land a real job internship(instead of Grubbins)
* 100's of internships available
* Learn how to start your own business out of High School making way more than minimum wage
* In college when interviewing for an internship don't be the guy that answers "no, sorry, this would be my first internship" putting you at a huge disadvantage"
* Fill in the Contact Us form at http://quillmarsh.com at the bottom left corner to find out more information

We will be evaluating design with this blog post in mind....
http://trovelinkdigest.com/color-influence-buyers/

We like attention grabbing contact us type stuff and calls to action. If you feel it is appropriate to change the marketing text to make your flyer stand out, please feel free. I am not the best at marketing and am the first to admit it.
Updates

A simple 8.5 x 11 flyer would be great.

Target Market(s)

High School students, male and female with high grade point averages(smart students). For the top 20% of their class.

Industry/Entity Type

Marketing

Requirements
Must have
• good call to action

```html
<!DOCTYPE html>
<html lang="en">
<head>
<meta charset="utf-8">
<title>Internships for 8th to 12th graders – quillmarsh</title>
<link href="https://fonts.googleapis.com/css2?family=Arimo:wght@400;700&display=swap" rel="stylesheet">
<style>
:root{
  --paper:#ffffff;
  --band:#858585;
  --ink:#4a4a4a;
  --headline:#1e73e8;
  --tick:#d4121a;
  --note-yellow:#f4ec5a;
  --note-cyan:#4fd3ee;
  --note-magenta:#f55cf0;
  --note-green:#63e24e;
  --accent-red:#e8202a;
  --accent-yellow:#f7f12a;
  --accent-green:#2fcf1e;
  --accent-blue:#1a4fe0;
  --link:#1a7bf0;
}
*{box-sizing:border-box;margin:0;padding:0}
html,body{width:964px;height:1200px;overflow:hidden;background:var(--paper)}
body{font-family:"Arimo",Arial,sans-serif;color:var(--ink)}
.flyer{position:relative;width:964px;height:1200px;overflow:hidden;background:var(--paper)}
.band{position:absolute;background:var(--band)}
.band--top{left:22px;top:0;width:903px;height:195px}
.band--second{left:22px;top:272px;width:903px;height:128px}
.band--third{left:22px;top:452px;width:540px;height:150px}
.band--right{left:490px;top:600px;width:435px;height:380px}
.band--bottom{left:22px;top:990px;width:903px;height:105px}

.headline{position:absolute;left:45px;top:140px;width:820px;transform:rotate(-10deg);transform-origin:left top;
  font-weight:700;font-size:68px;line-height:1.05;color:var(--headline);letter-spacing:2px;
  -webkit-text-stroke:2px #fff;paint-order:stroke fill;text-shadow:0 0 4px #fff}
.tick{position:absolute;left:590px;top:160px;width:95px;height:120px}

.note{position:absolute;display:flex;flex-direction:column;justify-content:center;align-items:center;
  text-align:center;padding:24px 30px;font-size:25px;line-height:1.35;color:var(--ink);
  text-shadow:0 0 2px #fff,0 0 2px #fff}
.note--yellow{left:430px;top:262px;width:470px;height:200px;background:var(--note-yellow);transform:rotate(-5deg);padding-left:90px}
.note--cyan{left:95px;top:378px;width:460px;height:222px;background:var(--note-cyan);transform:rotate(5deg)}
.note--magenta{left:322px;top:520px;width:600px;height:390px;background:var(--note-magenta);transform:rotate(-5deg);
  font-size:24px;justify-content:flex-start;padding:60px 30px 30px 110px}
.note--green{left:30px;top:760px;width:495px;height:320px;background:var(--note-green);transform:rotate(8deg);font-size:26px;padding:20px 30px}

.accent{font-weight:700}
.accent--red{color:var(--accent-red);font-size:44px}
.accent--yellow{color:var(--accent-yellow);font-size:44px}
.accent--green{color:var(--accent-green);font-size:42px}
.accent--blue{color:var(--accent-blue);font-size:46px}
.note__small{font-size:20px}

.call-to-action{position:absolute;left:40px;top:1125px;width:890px;text-align:center;font-size:22px;line-height:1.45;color:#8a8a8a}
.call-to-action__link{color:var(--link);font-size:34px;font-weight:700}
</style>
</head>
<body>
<main class="flyer">
  <div class="band band--top"></div>
  <div class="band band--second"></div>
  <div class="band band--third"></div>
  <div class="band band--right"></div>
  <div class="band band--bottom"></div>

  <h1 class="headline">Are you a student<br>in 8th to 12th<br>grade?!</h1>

  <svg class="tick" viewBox="0 0 95 120" aria-hidden="true">
    <path d="M6 78 L30 110 L90 6" fill="none" stroke="var(--tick)" stroke-width="11" stroke-linecap="round" stroke-linejoin="round"/>
  </svg>

  <section class="note note--yellow">
    <p><span class="accent accent--red">100's</span> of</p>
    <p>internships available</p>
  </section>

  <section class="note note--cyan">
    <p>Land a <span class="accent accent--yellow">real job</span> internship</p>
    <p class="note__small">instead of Grubbins</p>
  </section>

  <section class="note note--magenta">
    <p>Learn how to start your own business right out of high school making <span class="accent accent--green">way</span> more than</p>
    <p class="note__small">minimum wage</p>
  </section>

  <section class="note note--green">
    <p>In <span class="accent accent--blue">college</span> when interviewing for an internship don't be the guy that answers "no, sorry, this would be my first internship" putting you at a huge disadvantage</p>
  </section>

  <footer class="call-to-action">
    Fill in the Contact Us form at <span class="call-to-action__link">http://quillmarsh.com</span> at the<br>bottom left corner to find out more information
  </footer>
</main>
</body>
</html>
```